Brightwater Facility Partners Business card

We wish to have a professional Business card to present to large Corporate CEO's ASAP.

Our web site helps explain our business www.brightwaterfp.org

Brightwater Facility Partners was established after we discovered how difficult it is to organise outsourced services while heading up a business or company.

We act as a facilitator for businesses who don't have the desire, expertise or recourses to manage their own systems and meet all their requirements.

We provide an all in one facility management solution for all types of businesses. We manage schedules, contractors and costs on behalf of businesses and their needs and wants.

Having an extensive network ensures we are able to connect businesses with the right service providers.

Target Market(s)

Company CEO

Industry/Entity Type

Business

Font styles to use
Sans Serif

Colors
33a6d7
f9fdfe
0355a3

Requirements
Must have
• professional design
Nice to have
• colours to match logo

```html
<!DOCTYPE html>
<html lang="en">
<head>
<meta charset="utf-8">
<title>Brightwater Facility Partners – Business Card</title>
<link rel="stylesheet" href="https://fonts.googleapis.com/css2?family=Roboto+Slab:wght@400;600&display=swap">
<style>
  :root {
    --stage: #2c2c2c;
    --card: #f9fdfe;
    --card-shade: #edf1f4;
    --accent: #33a6d7;
    --deep-blue: #0355a3;
    --ink: #1d1f24;
    --muted: #5f6670;
  }
  * { box-sizing: border-box; margin: 0; padding: 0; }
  html, body {
    width: 1200px;
    height: 900px;
    overflow: hidden;
    background: var(--stage);
    font-family: "Roboto Slab", Georgia, serif;
  }
  .business-card {
    position: absolute;
    left: 160px;
    top: 192px;
    width: 880px;
    height: 516px;
    background: radial-gradient(ellipse at 30% 45%, var(--card-shade) 0%, var(--card) 70%);
  }
  .brand {
    position: absolute;
    left: 62px;
    top: 204px;
    display: flex;
    align-items: center;
    gap: 18px;
  }
  .brand-dot {
    width: 58px;
    height: 58px;
    border-radius: 50%;
    background: var(--deep-blue);
    flex: none;
  }
  .brand-name {
    font-weight: 600;
    font-size: 25px;
    line-height: 1.2;
    letter-spacing: 0.02em;
    text-transform: uppercase;
    color: var(--ink);
  }
  .divider {
    position: absolute;
    left: 522px;
    top: 32px;
    width: 2px;
    height: 452px;
    background: var(--accent);
  }
  .contact {
    position: absolute;
    left: 551px;
    top: 208px;
  }
  .contact-name {
    font-weight: 600;
    font-size: 26px;
    color: var(--accent);
    margin-bottom: 18px;
  }
  .contact-line {
    display: flex;
    align-items: center;
    gap: 10px;
    font-size: 19px;
    color: var(--ink);
    margin-bottom: 6px;
  }
  .contact-icon { width: 18px; height: 18px; flex: none; }
</style>
</head>
<body>
  <div class="business-card">
    <div class="brand">
      <span class="brand-dot"></span>
      <span class="brand-name">Brightwater<br>Facility Partners</span>
    </div>
    <div class="divider"></div>
    <div class="contact">
      <p class="contact-name">Daniel Harwood</p>
      <p class="contact-line">
        <svg class="contact-icon" viewBox="0 0 18 18" aria-hidden="true">
          <circle cx="9" cy="9" r="8" fill="none" stroke="#33a6d7" stroke-width="2"/>
          <path d="M6.3 5.2l1.4 1.6-.8 1.1c.5 1 1.2 1.7 2.2 2.2l1.1-.8 1.6 1.4-.7 1.3c-2.7-.3-5-2.6-5.3-5.3z" fill="#33a6d7"/>
        </svg>
        0400 123 987
      </p>
      <p class="contact-line">
        <svg class="contact-icon" viewBox="0 0 18 18" aria-hidden="true">
          <circle cx="9" cy="9" r="8" fill="none" stroke="#33a6d7" stroke-width="2"/>
          <rect x="5" y="6" width="8" height="6" fill="none" stroke="#33a6d7" stroke-width="1.2"/>
          <path d="M5 6l4 3.2L13 6" fill="none" stroke="#33a6d7" stroke-width="1.2"/>
        </svg>
        daniel@brightwaterfp.org
      </p>
    </div>
  </div>
</body>
</html>
```